Business card to promote business guidance

I need a card design to give to all my customers advertising a way to build a business exactly like the one they just bought from. I have an online store and will include one with each shipment. It should state the way to financial freedom and working for yourself

Target Market(s)

Young Entrepreneurs that want to start and don't know how

Industry/Entity Type

Business

Contact Information for Business Card

"You just bought from a successful company on Brindlemart. I have a unique business model, discovered by me, unlike any other that can make anyone successful. Follow me and message me for exactly the same model. If you ever wanted to work for yourself, I will teach you how. It's not a pipe dream, allow me to guide you out of the box."

Colors
85abd2

Requirements
Must have
• website www.dorianwelkby.example
instagram @thedorianwelkby

```html
<!DOCTYPE html>
<html lang="en">
<head>
<meta charset="utf-8">
<title>Dorian Welkby — Business Card</title>
<link href="https://fonts.googleapis.com/css2?family=Montserrat:wght@400;500;700;800&display=swap" rel="stylesheet">
<style>
  :root {
    --page-bg: #ecebe8;
    --card-front: #e6e6f3;
    --card-back: #7b9dca;
    --accent: #6f95cc;
    --ink: #4a4a55;
    --white: #ffffff;
    --shadow: rgba(40, 40, 60, 0.18);
  }
  * { box-sizing: border-box; margin: 0; padding: 0; }
  html, body {
    width: 1200px;
    height: 892px;
    overflow: hidden;
    background: var(--page-bg);
    font-family: "Montserrat", sans-serif;
  }
  .stage {
    position: relative;
    width: 1200px;
    height: 892px;
  }
  .card {
    position: absolute;
    width: 580px;
    height: 330px;
    border-radius: 22px;
    box-shadow: 0 10px 28px var(--shadow);
    display: flex;
    flex-direction: column;
    align-items: center;
    justify-content: center;
    text-align: center;
  }
  .card--front {
    left: 70px;
    top: 100px;
    background: var(--card-front);
  }
  .card--back {
    left: 550px;
    top: 462px;
    background: var(--card-back);
    color: var(--white);
    padding: 0 56px;
  }
  .owner-name {
    color: var(--accent);
    font-weight: 800;
    font-size: 27px;
    letter-spacing: 0.5px;
    text-transform: uppercase;
  }
  .owner-title {
    color: var(--ink);
    font-size: 17px;
    font-weight: 500;
    margin-top: 2px;
  }
  .divider {
    width: 40px;
    height: 4px;
    background: var(--accent);
    margin: 20px 0 22px;
  }
  .card--back .divider { background: var(--white); margin: 22px 0 18px; }
  .contact-list {
    display: flex;
    flex-direction: column;
    gap: 12px;
    align-items: flex-start;
  }
  .contact-item {
    display: flex;
    align-items: center;
    gap: 10px;
    color: var(--ink);
    font-size: 16px;
    font-weight: 500;
  }
  .contact-icon { width: 16px; height: 16px; flex: none; }
  .pitch {
    font-size: 14.5px;
    line-height: 1.62;
    font-weight: 500;
    letter-spacing: 0.2px;
  }
  .back-site {
    font-size: 16px;
    font-weight: 500;
  }
  .back-site strong { font-weight: 800; }
</style>
</head>
<body>
  <main class="stage">
    <section class="card card--front" aria-label="Card front">
      <h1 class="owner-name">Dorian Welkby</h1>
      <p class="owner-title">Managing Director</p>
      <span class="divider"></span>
      <ul class="contact-list">
        <li class="contact-item">
          <svg class="contact-icon" viewBox="0 0 16 16" aria-hidden="true">
            <rect x="1" y="1" width="14" height="14" rx="3" fill="var(--accent)"/>
          </svg>
          @thedorianwelkby
        </li>
        <li class="contact-item">
          <svg class="contact-icon" viewBox="0 0 16 16" aria-hidden="true">
            <circle cx="8" cy="8" r="7" fill="var(--accent)"/>
            <g fill="none" stroke="var(--card-front)" stroke-width="1.1">
              <ellipse cx="8" cy="8" rx="3" ry="7"/>
              <line x1="1" y1="8" x2="15" y2="8"/>
              <line x1="2.5" y1="4.5" x2="13.5" y2="4.5"/>
              <line x1="2.5" y1="11.5" x2="13.5" y2="11.5"/>
            </g>
          </svg>
          www.dorianwelkby.example
        </li>
      </ul>
    </section>

    <section class="card card--back" aria-label="Card back">
      <p class="pitch">You just bought from a successful company on Brindlemart. I have a unique business model, discovered by me, unlike any other that can make anyone successful. Follow me and message me for exactly the same model. If you ever wanted to work for yourself, I will teach you how. It's not a pipe dream, allow me to guide you out of the box.</p>
      <span class="divider"></span>
      <p class="back-site">www.<strong>dorianwelkby</strong>.example</p>
    </section>
  </main>
</body>
</html>
```